Fair Lend Guide's Mortgage Lantern

For FairLendGuide.org - Creating a sequence of web pages for consumers to understand their mortgage through Mortgage Lantern. There are six pages - want the designer to be willing to design and code those six pages. Most of the pages are very similar.

```html
<!DOCTYPE html>
<html lang="en">
<head>
<meta charset="utf-8">
<title>Fair Lend Guide – Mortgage Lantern</title>
<link href="https://fonts.googleapis.com/css2?family=Montserrat:wght@400;500;600&family=Mulish:wght@700;800&display=swap" rel="stylesheet">
<style>
  :root {
    --topbar: #1b80d8;
    --header: #0b25c9;
    --hero-a: #2f4ef0;
    --hero-b: #2440e2;
    --footer: #1567c9;
    --login: #16c27c;
    --white: #ffffff;
    --card-fill: rgba(255, 255, 255, 0.2);
    --card-line: rgba(255, 255, 255, 0.9);
  }
  * { box-sizing: border-box; margin: 0; padding: 0; }
  html, body { width: 1200px; height: 639px; overflow: hidden; }
  body { position: relative; font-family: "Montserrat", sans-serif; color: var(--white); background: var(--hero-b); }

  .topbar { position: absolute; top: 0; left: 0; width: 1200px; height: 50px; background: var(--topbar); }
  .login-button {
    position: absolute; left: 509px; top: 8px; width: 74px; height: 34px;
    background: var(--login); border: 1px solid rgba(255,255,255,0.6);
    font: 500 15px "Montserrat", sans-serif; color: var(--white);
    display: flex; align-items: center; justify-content: center;
  }

  .site-header { position: absolute; top: 50px; left: 0; width: 1200px; height: 87px; background: var(--header); }
  .brand { position: absolute; left: 156px; top: 0; height: 87px; display: flex; align-items: center; gap: 10px; }
  .brand-mark { width: 40px; height: 40px; border-radius: 6px; background: var(--white); }
  .brand-name { font: 500 20px "Montserrat", sans-serif; color: var(--white); }
  .main-nav { position: absolute; left: 610px; top: 0; height: 87px; display: flex; align-items: center; gap: 25px; font-size: 13.5px; font-weight: 500; }
  .main-nav .caret { display: inline-block; margin-left: 4px; border: 3.5px solid transparent; border-top-color: var(--white); vertical-align: 0; }

  .hero-backdrop { position: absolute; top: 137px; left: 0; width: 1200px; height: 448px;
    background: linear-gradient(135deg, var(--hero-a) 0%, var(--hero-b) 55%, #2a46ea 100%); }

  .option-card {
    position: absolute; width: 214px; height: 105px;
    background: var(--card-fill); border: 1px solid var(--card-line); border-radius: 6px;
    display: flex; align-items: center; justify-content: center; text-align: center;
    font: 800 17.5px/1.65 "Mulish", sans-serif; color: var(--white);
  }
  .option-card.is-active { border: 2px solid var(--white); box-shadow: 0 0 10px rgba(255,255,255,0.8); }
  .row-1 { top: 218px; } .row-2 { top: 373px; }
  .col-1 { left: 111px; } .col-2 { left: 365px; } .col-3 { left: 620px; } .col-4 { left: 873px; }

  .site-footer { position: absolute; top: 585px; left: 0; width: 1200px; height: 54px; background: var(--footer); font-size: 10px; }
  .copyright { position: absolute; left: 153px; top: 21px; }
  .social-links { position: absolute; left: 555px; top: 12px; display: flex; gap: 3px; }
  .social-dot { width: 29px; height: 29px; border-radius: 50%; background: rgba(255,255,255,0.35); }
  .legal-links { position: absolute; left: 873px; top: 21px; }
  .legal-links .divider { margin: 0 7px; }
</style>
</head>
<body>
  <div class="topbar">
    <div class="login-button">LOG IN</div>
  </div>

  <header class="site-header">
    <div class="brand">
      <span class="brand-mark"></span>
      <span class="brand-name">FairLendGuide</span>
    </div>
    <nav class="main-nav">
      <span>Home</span>
      <span>Testimonials</span>
      <span>Programs</span>
      <span>FAQ<i class="caret"></i></span>
      <span>Blog</span>
      <span>Podcast</span>
    </nav>
  </header>

  <div class="hero-backdrop" role="img" aria-label="Blue background with faint overlapping geometric facets"></div>

  <main>
    <div class="option-card row-1 col-1">Edit Mortgage<br>Profile</div>
    <div class="option-card row-1 col-2">Maximum Mortgage<br>Qualification</div>
    <div class="option-card row-1 col-3">Specific Mortgage<br>Amount</div>
    <div class="option-card row-1 col-4">Specific Mortgage<br>Payment</div>
    <div class="option-card row-2 col-1 is-active">Conventional Mortgage<br>Option</div>
    <div class="option-card row-2 col-2">FHA Mortgage<br>Option</div>
    <div class="option-card row-2 col-3">VA Mortgage<br>Option</div>
    <div class="option-card row-2 col-4">USDA Mortgage<br>Option</div>
  </main>

  <footer class="site-footer">
    <span class="copyright">Copyright 2023 by Fair Lend Guide</span>
    <div class="social-links">
      <span class="social-dot"></span>
      <span class="social-dot"></span>
      <span class="social-dot"></span>
    </div>
    <span class="legal-links">Terms Of Use<span class="divider">|</span>Privacy Statement</span>
  </footer>
</body>
</html>
```